We need a website that entices australia's workers to sign up to help protect their industry and their jobs. The key message is "Backing Australian Work" and that headline / tagline should feature prominently on the site.

In terms of style I lack the current 'scrolling' style (see example http://www.fieldmarkweb.ca )

The site must dynamically for mobile platforms. It must also use Quenda or Paperloft as CMS so is client editable.

The attached logo is the basis for the design and the name of the organisation is the Enduring Progress Council. Please make an allowance for an iframe embed (min height 650px) see attached sample.

It should also have a subscriber sign up for that connects with Mailbridge Relay

Attached text for front page is DRAFT ONLY

Target Market(s)

Working class australians, (eg miners, farmers, factory workers, etc)

Industry/Entity Type

Industry

Coding

Coded - Design and coding required

Number of Pages Required

4 page

Requirements
Must have
• An editable CMS
• Subscription form connecting with Mailbridge Relay (see https://kovalpint.sendquill.com/help/topic.aspx?t=13)
• Must resize for mobile
• Must allow for an iframe
Nice to have
• It must have a friendly feel but strong, not 'girly' though should not alienate women
Should not have
• Images that are not australian
• Images that do not have the appropriate rights to use

```html
<!DOCTYPE html>
<html lang="en">
<head>
<meta charset="utf-8">
<title>Backing Australian Work</title>
<link rel="stylesheet" href="https://fonts.googleapis.com/css2?family=Open+Sans:ital,wght@0,300;0,400;0,600;1,600&display=swap">
<style>
  :root {
    --navy-deep: #121d38;
    --navy-mid: #1f2c4d;
    --harbour-glow: #6a6560;
    --water: #1b2a45;
    --orange: #f05a24;
    --amber: #f9a61b;
    --white: #ffffff;
    --page-grey: #f2f2f2;
    --ink: #333333;
    --ink-soft: #555555;
  }
  * { box-sizing: border-box; margin: 0; padding: 0; }
  html, body { width: 1200px; height: 1000px; overflow: hidden; }
  body {
    font-family: "Open Sans", sans-serif;
    background: var(--page-grey);
    position: relative;
  }
  .hero {
    position: absolute;
    inset: 0 0 auto 0;
    height: 846px;
    clip-path: polygon(0 0, 100% 0, 100% 845px, 0 778px);
  }
  .hero-photo {
    position: absolute;
    inset: 0;
    background: linear-gradient(180deg,
      var(--navy-deep) 0%,
      var(--navy-mid) 40%,
      var(--harbour-glow) 62%,
      #3b3f4c 72%,
      var(--water) 85%,
      var(--navy-deep) 100%);
  }
  .site-header {
    position: absolute;
    top: 0; left: 0; right: 0;
    height: 140px;
  }
  .brand {
    position: absolute;
    left: 30px; top: 44px;
    display: flex;
    align-items: center;
    gap: 14px;
  }
  .brand-dot {
    width: 56px; height: 56px;
    border-radius: 50%;
    background: var(--orange);
  }
  .brand-name {
    font-size: 18px;
    font-weight: 400;
    line-height: 22px;
    color: var(--white);
    width: 150px;
  }
  .main-nav {
    position: absolute;
    right: 31px; top: 60px;
    display: flex;
    gap: 47px;
  }
  .main-nav a {
    font-size: 19px;
    font-weight: 400;
    color: var(--white);
    text-decoration: none;
  }
  .main-nav a.is-active { color: var(--amber); }
  .hero-content {
    position: absolute;
    top: 274px; left: 0; right: 0;
    text-align: center;
    color: var(--white);
  }
  .hero-title {
    font-size: 59px;
    font-weight: 600;
    line-height: 78px;
  }
  .hero-lede {
    margin-top: 22px;
    font-size: 34px;
    font-weight: 300;
    line-height: 45px;
  }
  .hero-cta {
    position: absolute;
    left: 382px; top: 569px;
    width: 436px; height: 50px;
    border: 1px solid var(--orange);
    color: var(--orange);
    font-size: 20px;
    font-weight: 600;
    text-decoration: none;
    text-transform: uppercase;
    display: flex;
    align-items: center;
    justify-content: center;
  }
  .intro {
    position: absolute;
    left: 93px; top: 906px;
    width: 1080px;
  }
  .intro-heading {
    font-size: 25px;
    font-style: italic;
    font-weight: 600;
    letter-spacing: -0.4px;
    line-height: 30px;
    color: var(--ink);
    text-transform: uppercase;
    white-space: nowrap;
  }
  .intro-text {
    margin-top: 20px;
    font-size: 16px;
    color: var(--ink-soft);
    text-transform: uppercase;
    white-space: nowrap;
  }
</style>
</head>
<body>
  <section class="hero">
    <div class="hero-photo" role="img" aria-label="Night photograph of a bridge under construction over water, with a tall crane and city lights"></div>

    <header class="site-header">
      <div class="brand">
        <span class="brand-dot"></span>
        <span class="brand-name">Backing Australian Work</span>
      </div>
      <nav class="main-nav">
        <a href="#" class="is-active">Take Action</a>
        <a href="#">About</a>
        <a href="#">Facts</a>
        <a href="#">News</a>
        <a href="#">Contact</a>
      </nav>
    </header>

    <div class="hero-content">
      <h1 class="hero-title">MY FAMILY COMES FIRST</h1>
      <p class="hero-lede">I care for the environment – but not at the cost of my job,<br>our savings or our retirement</p>
    </div>

    <a href="#" class="hero-cta">Take action to protect your family</a>
  </section>

  <section class="intro">
    <h2 class="intro-heading">The greenies want your bank and your super fund to stop investing in mining,<br>agriculture and other industries that are the backbone of Australia.</h2>
    <p class="intro-text">While they are trying to ‘do good’ if they are successful their actions will severely impact the lives of everyday</p>
  </section>
</body>
</html>
```